B.L.W.T. Business Card Design

we need a business card design for a motor vehicle repair business in Southport Australia, called Dravo's Automotive Repair Services. Our services include panel & paint, resprays and light bodyworks. We have a logo which we would like to use on the business card. We would like to see designs that use the colours blue and grey.

Industry/Entity Type

Automotive

Contact Information for Business Card

Dravo's Automotive Repair Services,
Merrin Folke,
7/2-5 Tralby Street Southport 4215, 0468 732 180, /dravosautomotiverepairservices, dravosautomotiverepairservices@quellmail.example,
services: panel & paint, respray, light bodyworks.
ABN: 47 206 519 782

Requirements
Must have
• Front of card must include attached logo and contact details.
please list services
Your eye should be drawn to the name (Merrin Folke) and phone number (0468 732 180).
Font must be legible and contemporary.
back of business card should have the following:
1. title - quote and
2. list the following: for, date, valid till, quote details and
3. a footer "to book you repair, please contact Merrin Folke on 0468 732 180".
There needs to be enough space to hand write details.
Should not have
• do not include any graphics/illustrations.

```html
<!DOCTYPE html>
<html lang="en">
<head>
<meta charset="utf-8">
<title>Repair Quote</title>
<link rel="stylesheet" href="https://fonts.googleapis.com/css2?family=Source+Sans+3:wght@400;700&display=swap">
<style>
  :root {
    --band-grey: #595959;
    --rule-grey: #3a3a3a;
    --ink: #1e1e1e;
    --paper: #ffffff;
    --label-white: #ffffff;
  }
  html, body {
    margin: 0;
    padding: 0;
    overflow: hidden;
    background: var(--paper);
  }
  .quote-card {
    position: relative;
    width: 1200px;
    height: 758px;
    overflow: hidden;
    background: var(--paper);
    font-family: "Source Sans 3", "Myriad Pro", Arial, sans-serif;
    color: var(--ink);
  }
  .title-band {
    position: absolute;
    left: 15px;
    top: 0;
    width: 1157px;
    height: 92px;
    background: var(--band-grey);
    border-radius: 0 0 24px 24px;
    box-shadow: 3px 5px 7px rgba(0, 0, 0, 0.35);
    display: flex;
    align-items: flex-end;
    justify-content: center;
  }
  .title-band h1 {
    margin: 0 0 12px;
    font-weight: 400;
    font-size: 62px;
    line-height: 1;
    color: var(--label-white);
    letter-spacing: 0.5px;
  }
  .write-line {
    position: absolute;
    left: 12px;
    width: 1155px;
    height: 0;
    border-top: 1.3px solid var(--rule-grey);
  }
  .mark {
    position: absolute;
    top: 502px;
    font-weight: 700;
    font-size: 44px;
    line-height: 1;
    color: var(--ink);
    transform: translateX(-50%);
  }
  .label-bar {
    position: absolute;
    left: 12px;
    top: 562px;
    width: 1156px;
    height: 50px;
    background: var(--band-grey);
  }
  .label-bar span {
    position: absolute;
    top: 0;
    font-size: 35px;
    line-height: 50px;
    color: var(--label-white);
    transform: translateX(-50%);
    white-space: nowrap;
  }
  .booking {
    position: absolute;
    left: 0;
    width: 1200px;
    text-align: center;
    margin: 0;
    line-height: 1;
    white-space: nowrap;
  }
  .booking-lead {
    top: 651px;
    font-size: 40px;
    font-weight: 400;
  }
  .booking-contact {
    top: 697px;
    font-size: 49px;
    font-weight: 700;
    letter-spacing: 2.5px;
  }
</style>
</head>
<body>
  <main class="quote-card">
    <header class="title-band"><h1>QUOTE</h1></header>

    <div class="write-line" style="top:233px"></div>
    <div class="write-line" style="top:315px"></div>
    <div class="write-line" style="top:394px"></div>
    <div class="write-line" style="top:477px"></div>

    <span class="mark" style="left:103px">/</span>
    <span class="mark" style="left:206px">/</span>
    <span class="mark" style="left:533px">/</span>
    <span class="mark" style="left:635px">/</span>
    <span class="mark" style="left:966px">$</span>
    <span class="mark" style="left:1105px">•</span>

    <div class="label-bar">
      <span style="left:140px">date</span>
      <span style="left:563px">valid till</span>
    </div>

    <p class="booking booking-lead">To book your repair please contact</p>
    <p class="booking booking-contact">Merrin Folke on 0468 732 180</p>
  </main>
</body>
</html>
```